We need a redesign of our current website: www.halvardgroupsite.com. Halvard Group is a fully integrated hospitality development, management, and investment firm. We strive for leadership in each of our segments by building quality assets, exacting high standards of customer service, and focusing on returns for our investors and partners.

It is our mission to provide our guests an exceptional lodging experience; our clients an unsurpassed level of management in their properties; and create positive returns for our investors and partners. We achieve our mission via a company culture of transparency, ownership of our actions, and accountability for our results.

Target Market(s)

hotel owners, hotel developers, hotel investors, bankers

Industry/Entity Type

Hospitality

Requirements
Must have
• Our logo has to be there along with the quote and the ability to convey the following quote off of our current website: "Halvard was founded on the principles of integrity, honesty, loyalty, and trust. These convictions embody our company at every level, and show in every action."

```html
<!DOCTYPE html>
<html lang="en">
<head>
<meta charset="utf-8">
<title>Halvard Group</title>
<link rel="stylesheet" href="https://fonts.googleapis.com/css2?family=Satisfy&family=Delius&family=Lora:ital,wght@1,400;1,600&family=Montserrat:wght@500&display=swap">
<style>
  :root {
    --page: #333132;
    --logo-panel: #d6d6d6;
    --brand-orange: #d27a22;
    --brand-dark: #1e1e1e;
    --text-light: #ffffff;
    --footer: #000000;
    --footer-text: #a9a9a9;
    --button: #f07410;
    --button-text: #1a1a1a;
    --caption-bg: rgba(30, 22, 22, 0.82);
  }
  * { box-sizing: border-box; margin: 0; padding: 0; }
  html, body { width: 1200px; height: 900px; overflow: hidden; background: var(--page); }
  body { position: relative; font-family: "Lora", Georgia, serif; color: var(--text-light); }

  .brand {
    position: absolute; left: 23px; top: 32px; width: 466px; height: 101px;
    background: var(--logo-panel); z-index: 2;
    display: flex; align-items: center; gap: 22px; padding-left: 26px;
  }
  .brand-dot { width: 56px; height: 56px; border-radius: 50%; background: var(--brand-orange); flex: none; }
  .brand-name {
    font-family: "Montserrat", Arial, sans-serif; font-weight: 500;
    font-size: 44px; letter-spacing: 3px; color: var(--brand-dark); text-transform: uppercase;
  }

  .main-nav { position: absolute; top: 76px; left: 515px; display: flex; gap: 31px; z-index: 2; }
  .main-nav a {
    font-family: "Satisfy", cursive; font-size: 23px; color: var(--text-light);
    text-decoration: none; text-shadow: 2px 2px 2px #000;
  }

  .hero {
    position: absolute; left: 100px; top: 112px; width: 1000px; height: 338px;
    border-radius: 0 26px 26px 0; overflow: hidden;
    background: linear-gradient(100deg, #e9e2d6 0%, #d8cbb9 28%, #8a4a2c 32%, #a45a34 55%, #7d3f33 72%, #c8b6ac 88%, #efe4dc 100%);
  }
  .hero-quote {
    position: absolute; left: 0; bottom: 0; width: 600px; height: 75px;
    background: var(--caption-bg); padding: 6px 12px;
    font-family: "Satisfy", cursive; font-size: 16px; line-height: 22px;
  }

  .intro { position: absolute; left: 102px; top: 490px; width: 356px; }
  .section-title {
    font-family: "Satisfy", cursive; font-size: 27px; letter-spacing: 2px;
    text-transform: uppercase; text-shadow: 2px 2px 2px #000; font-weight: 400;
  }
  .section-text { font-size: 12.4px; line-height: 15px; font-weight: 600; font-style: italic; margin-top: 14px; }
  .mission { margin-top: 22px; }

  .feature { position: absolute; top: 490px; width: 298px; text-align: center; }
  .feature-title { font-family: "Delius", cursive; font-size: 22px; font-weight: 400; letter-spacing: 1px; }
  .feature-media {
    display: block; margin-top: 14px; height: 193px;
    border: 3px solid #fff; border-radius: 4px;
  }
  .hospitality { left: 470px; }
  .hospitality .feature-media { background: linear-gradient(180deg, #5d8fc9 0%, #b79a78 45%, #7b5a3c 75%, #3a76a8 100%); }
  .investment { left: 790px; }
  .investment .feature-media { background: linear-gradient(180deg, #ffffff 0%, #eef3f6 50%, #7cc4ea 85%, #e8f4fb 100%); }

  .read-more {
    position: absolute; top: 740px; width: 183px; height: 42px;
    background: var(--button); border: 2px solid #fff;
    font-family: "Delius", cursive; font-size: 21px; color: var(--button-text);
    text-decoration: none; display: flex; align-items: center; justify-content: center;
    letter-spacing: 1px; box-shadow: 2px 2px 3px #000;
  }
  .read-more.hospitality-link { left: 583px; }
  .read-more.investment-link { left: 904px; }

  .site-footer {
    position: absolute; left: 23px; top: 800px; width: 1158px; height: 70px;
    background: var(--footer); display: flex; align-items: center;
  }
  .footer-dot { position: absolute; left: 4px; top: -14px; width: 60px; height: 60px; border-radius: 50%; background: var(--brand-orange); }
  .footer-text {
    margin-left: 81px; font-family: "Lora", Georgia, serif; font-style: italic;
    font-size: 16px; letter-spacing: 4.2px; color: var(--footer-text);
  }
</style>
</head>
<body>
  <header>
    <div class="brand">
      <span class="brand-dot"></span>
      <span class="brand-name">Halvard Group</span>
    </div>
    <nav class="main-nav">
      <a href="#">Home</a>
      <a href="#">Services</a>
      <a href="#">Invesments</a>
      <a href="#">Hospitality</a>
      <a href="#">Contact Us</a>
    </nav>
  </header>

  <section class="hero" role="img" aria-label="Hotel interior photograph: bed with white pillows, wooden lattice wall and design material samples">
    <p class="hero-quote">Halvard was founded on the principles of integrity,honesty, loyalty, and trust. These convictions embody our company at every level, and show in every action."</p>
  </section>

  <section class="intro">
    <h2 class="section-title">About Us</h2>
    <p class="section-text">Halvard Group is a fully integrated hospitality development, management, and investment firm. We strive for leadership in each of our segments by building quality assets, exacting high standards of customer service, and focusing on returns for our investors and partners.</p>
    <h2 class="section-title mission">Our Mission</h2>
    <p class="section-text">It is our mission to provide our guests an exceptional lodging experience; our clients an unsurpassed level of management in their properties; and create positive returns for our investors and partners. We achieve our mission via a company culture of transparency, ownership of our actions and accountability for our results.</p>
  </section>

  <section class="feature hospitality">
    <h3 class="feature-title">Hospitality Development</h3>
    <span class="feature-media" role="img" aria-label="Photograph of a resort hotel with palm trees and pool at dusk"></span>
  </section>
  <section class="feature investment">
    <h3 class="feature-title">Invesment Plans</h3>
    <span class="feature-media" role="img" aria-label="Illustration of business people on a rising bar chart with a green growth arrow"></span>
  </section>

  <a class="read-more hospitality-link" href="#">Read More &gt;&gt;&gt;</a>
  <a class="read-more investment-link" href="#">Read More &gt;&gt;&gt;</a>

  <footer class="site-footer">
    <span class="footer-dot"></span>
    <p class="footer-text">2012 © Copyright HALVARD GROUP. all right reserved. Read legal policy and licence</p>
  </footer>
</body>
</html>
```